Bluewater Products Flyer

Bluewater Lending Group, Inc.
Licensed Mortgage Company
Serving the DMV since 1997
"You choose Bluewater, we'll carry it home"
We specialize in...
FHA Loans
* Credit Scores as low as 500
* 203K Renovation Loans
Conventional Loans
* As little as 1% Down
* Bank Statement for Self-Employed
Investor Loans
* DSCR, & Fix & Flip
* Commercial & New Construction
Other Programs
* HELOCS & Reverse Mortgages
Call today for a free consultation
(800) 641-2957
www.bluewaterlendhub.com
NMLS #731846

```html
<!DOCTYPE html>
<html lang="en">
<head>
<meta charset="utf-8">
<title>Bluewater Products Flyer</title>
<link rel="stylesheet" href="https://fonts.googleapis.com/css2?family=Montserrat:wght@400;500;700;800;900&display=swap">
<style>
  :root {
    --purple-deep: #3a0ca3;
    --purple-mid: #5b2fd1;
    --purple-bar: #3d0fa8;
    --gold: #e8b04f;
    --gold-text: #f0b648;
    --ink: #2a2438;
    --white: #ffffff;
    --paper: #f7f7f9;
    --backdrop: #e4e4e6;
  }
  * { margin: 0; padding: 0; box-sizing: border-box; }
  html, body {
    width: 1200px; height: 2505px; overflow: hidden;
    background: var(--backdrop);
    font-family: "Montserrat", sans-serif;
  }
  .flyer {
    position: absolute; left: 50px; top: 476px;
    width: 907px; height: 1281px;
    background: var(--paper);
    transform: scale(1.2128); transform-origin: top left;
    box-shadow: 0 6px 18px rgba(0,0,0,0.18);
    overflow: hidden;
  }
  .top-bar { position: absolute; left: 44px; top: 55px; width: 467px; height: 23px; background: var(--purple-bar); }
  .hero-photo {
    position: absolute; left: 0; top: 78px; width: 907px; height: 535px;
    background: linear-gradient(90deg, #6a45b8 0%, #7b58c6 45%, #8a6ad0 62%, #9a86d6 100%);
  }
  .headline {
    position: absolute; left: 64px; top: 218px; height: 225px;
    border-left: 11px solid var(--white);
    padding-left: 17px;
    font-weight: 900; font-size: 52px; line-height: 50px;
    text-transform: uppercase; letter-spacing: -0.5px;
    padding-top: 13px;
  }
  .headline .accent { color: var(--gold-text); display: block; }
  .headline .plain { color: var(--white); display: block; }

  .card {
    position: absolute; width: 226px; height: 272px;
    background: linear-gradient(180deg, var(--purple-mid) 0%, var(--purple-deep) 100%);
    color: var(--white);
    padding: 32px 18px 0 28px;
  }
  .card.fha { left: 44px; top: 546px; border-top-left-radius: 22px; }
  .card.conventional { left: 285px; top: 546px; border-top-right-radius: 22px; }
  .card.investor { left: 44px; top: 834px; border-bottom-left-radius: 22px; }
  .card.other { left: 285px; top: 834px; border-bottom-right-radius: 22px; }
  .card-icon { display: block; margin: 0 auto 8px; width: 50px; height: 52px; transform: translateX(-5px); }
  .card-title { text-align: center; font-weight: 800; font-size: 25px; line-height: 22px; margin-bottom: 16px; transform: translateX(-5px); }
  .card-list { list-style: none; font-size: 17px; line-height: 16px; font-weight: 500; }
  .card-list li { position: relative; padding-left: 16px; margin-bottom: 13px; }
  .card-list li::before { content: ""; position: absolute; left: 0; top: 5px; width: 8px; height: 8px; border-radius: 50%; background: var(--white); }

  .specialize-tag {
    position: absolute; left: 156px; top: 800px; width: 242px; height: 50px;
    background: var(--gold); color: var(--purple-deep);
    font-weight: 800; font-size: 22px; line-height: 50px; text-align: center;
  }

  .company-info {
    position: absolute; left: 530px; top: 686px; width: 354px;
    text-align: center; color: var(--ink); font-size: 20.5px; line-height: 31px;
  }
  .company-info .nmls { color: var(--purple-deep); font-weight: 500; }
  .cta {
    position: absolute; left: 549px; top: 833px; width: 309px; height: 78px;
    background: var(--gold); color: var(--purple-deep);
    font-weight: 800; font-size: 21px; line-height: 22px; text-align: center;
    padding-top: 17px;
  }
  .brand-mark {
    position: absolute; left: 574px; top: 945px; width: 259px; height: 160px;
    background: var(--white);
    display: flex; align-items: center; justify-content: center; gap: 10px;
  }
  .brand-dot { width: 22px; height: 22px; border-radius: 50%; background: var(--purple-deep); }
  .brand-name { font-weight: 800; font-size: 30px; color: var(--purple-deep); }

  .footer {
    position: absolute; left: 0; top: 1156px; width: 907px; height: 125px;
  }
  .footer svg.band { position: absolute; inset: 0; }
  .footer-address {
    position: absolute; left: 40px; top: 38px; display: flex; align-items: center; gap: 8px;
    color: var(--white); font-size: 17px; line-height: 18px;
  }
  .footer-web {
    position: absolute; left: 292px; top: 30px; width: 320px; text-align: center;
    color: var(--purple-deep); font-size: 19.5px; font-weight: 500;
  }
  .footer-web svg { display: block; margin: 0 auto 6px; }
  .footer-phone {
    position: absolute; left: 664px; top: 36px; display: flex; align-items: center; gap: 12px;
    color: var(--white);
  }
  .footer-phone .label { font-size: 14.5px; line-height: 16px; }
  .footer-phone .number { font-size: 21px; font-weight: 800; line-height: 22px; }
</style>
</head>
<body>
<main class="flyer">
  <div class="top-bar"></div>
  <div class="hero-photo" role="img" aria-label="Photo of a smiling family holding a red Home For Sale sign, over a soft purple-tinted close-up of the family"></div>

  <h1 class="headline">
    <span class="accent">You choose</span>
    <span class="accent">Bluewater,</span>
    <span class="plain">We'll carry</span>
    <span class="plain">it home</span>
  </h1>

  <section class="card fha">
    <svg class="card-icon" viewBox="0 0 50 52"><path d="M18 6h14l-4 8h-6z" fill="#fff"/><path d="M25 14c-12 0-19 12-19 22 0 9 8 13 19 13s19-4 19-13c0-10-7-22-19-22z" fill="#fff"/><text x="25" y="41" font-family="Montserrat,sans-serif" font-weight="800" font-size="16" fill="#3a0ca3" text-anchor="middle">%</text></svg>
    <h2 class="card-title">FHA Loans</h2>
    <ul class="card-list">
      <li>Credit Scores as low as 500</li>
      <li>203K Renovation Loans</li>
    </ul>
  </section>

  <section class="card conventional">
    <svg class="card-icon" viewBox="0 0 50 52"><path d="M20 4h12l-3 7h-6z" fill="#fff"/><path d="M26 11c-9 0-14 9-14 17 0 3 1 5 2 7h22c2-2 3-4 3-7 0-8-5-17-13-17z" fill="#fff"/><path d="M4 38l8-4h10l6 4-6 4H12z" fill="#fff"/><circle cx="37" cy="40" r="9" fill="#fff"/><path d="M33 40l3 3 5-6" stroke="#3a0ca3" stroke-width="2.5" fill="none"/></svg>
    <h2 class="card-title">Conventional Loans</h2>
    <ul class="card-list">
      <li>As little as 1% Down</li>
      <li>Bank Statement for Self-Employed</li>
    </ul>
  </section>

  <section class="card investor">
    <svg class="card-icon" viewBox="0 0 50 52"><circle cx="17" cy="9" r="7" fill="#fff"/><circle cx="33" cy="9" r="7" fill="#fff"/><text x="17" y="13" font-family="Montserrat,sans-serif" font-weight="800" font-size="10" fill="#3a0ca3" text-anchor="middle">$</text><text x="33" y="13" font-family="Montserrat,sans-serif" font-weight="800" font-size="10" fill="#3a0ca3" text-anchor="middle">$</text><circle cx="25" cy="24" r="5" fill="#fff"/><circle cx="12" cy="27" r="4" fill="#fff"/><circle cx="38" cy="27" r="4" fill="#fff"/><path d="M16 46c0-8 4-14 9-14s9 6 9 14z" fill="#fff"/><path d="M4 44c0-6 3-11 8-11s6 3 6 5v6z" fill="#fff"/><path d="M46 44c0-6-3-11-8-11s-6 3-6 5v6z" fill="#fff"/></svg>
    <h2 class="card-title">Investor Loans</h2>
    <ul class="card-list">
      <li>DSCR, &amp; Fix &amp; Flip</li>
      <li>Commercial &amp; New Construction</li>
    </ul>
  </section>

  <section class="card other">
    <svg class="card-icon" viewBox="0 0 50 52"><circle cx="25" cy="22" r="18" fill="none" stroke="#fff" stroke-width="3"/><ellipse cx="25" cy="22" rx="8" ry="18" fill="none" stroke="#fff" stroke-width="2.5"/><path d="M7 22h36M10 13h30M10 31h30" stroke="#fff" stroke-width="2.5"/><path d="M8 40l10-6h14l10 6-8 8H16z" fill="#fff"/></svg>
    <h2 class="card-title">Other Programs</h2>
    <ul class="card-list">
      <li>HELOCS &amp; Reverse Mortgages</li>
    </ul>
  </section>

  <div class="specialize-tag">We specialize in...</div>

  <div class="company-info">
    <p>Bluewater Lending Group, Inc.</p>
    <p>Licensed Mortgage Company</p>
    <p>Serving the DMV since 1997</p>
    <p class="nmls">NMLS #731846</p>
  </div>

  <div class="cta">Call today for a<br>free consultation</div>

  <div class="brand-mark">
    <span class="brand-dot"></span>
    <span class="brand-name">Bluewater</span>
  </div>

  <footer class="footer">
    <svg class="band" width="907" height="125" viewBox="0 0 907 125">
      <defs>
        <linearGradient id="footerFill" x1="0" y1="0" x2="0" y2="1">
          <stop offset="0" stop-color="#5b2fd1"/>
          <stop offset="1" stop-color="#3a0ca3"/>
        </linearGradient>
      </defs>
      <rect width="907" height="125" fill="url(#footerFill)"/>
      <polygon points="242,0 592,0 665,125 307,125" fill="#e8b04f"/>
    </svg>
    <div class="footer-address">
      <svg width="26" height="34" viewBox="0 0 26 34"><path d="M13 2C7 2 3 6.5 3 12c0 7 10 18 10 18s10-11 10-18C23 6.5 19 2 13 2z" fill="none" stroke="#fff" stroke-width="3"/><circle cx="13" cy="12" r="4" fill="#fff"/><ellipse cx="13" cy="31" rx="9" ry="2.5" fill="#fff"/></svg>
      <span>2180 Harbor Point Rd,<br>Columbia, MD 21044</span>
    </div>
    <div class="footer-web">
      <svg width="24" height="24" viewBox="0 0 24 24"><circle cx="12" cy="12" r="10" fill="#3a0ca3"/><ellipse cx="12" cy="12" rx="4" ry="10" fill="none" stroke="#e8b04f" stroke-width="1.6"/><path d="M2 12h20M4 7h16M4 17h16" stroke="#e8b04f" stroke-width="1.6"/></svg>
      www.bluewaterlendhub.com
    </div>
    <div class="footer-phone">
      <svg width="30" height="30" viewBox="0 0 30 30"><path d="M7 3l5 6-3 3c1 4 5 8 9 9l3-3 6 5-3 4C14 27 3 16 3 6z" fill="none" stroke="#fff" stroke-width="2.5" stroke-linejoin="round"/><path d="M18 4a9 9 0 0 1 8 8M18 9a4 4 0 0 1 3 3" stroke="#fff" stroke-width="2.2" fill="none"/></svg>
      <div>
        <div class="label">Call Toll Free:</div>
        <div class="number">(800)-641-2957</div>
      </div>
    </div>
  </footer>
</main>
</body>
</html>
```